Business Card for Business consulting practice

Need a design for a consultant business card. Simple and elegant.
I need the following information on the card:
Logo: (see uploaded file)
Company name: Calmora Advisory Group
Name: Dana Weltrup
Title: Managing Director - Aerospace and Defence
Phone #: 514-268-3917
e-mail: dana.weltrup@calmora-example.com
Website: www.calmora-example.com
Tagline: Proposals Management and Capture support for complex procurements

```html
<!DOCTYPE html>
<html lang="es">
<head>
<meta charset="utf-8">
<title>Calmora Advisory Group – Tarjeta de presentación</title>
<link rel="stylesheet" href="https://fonts.googleapis.com/css2?family=Raleway:wght@500;600;700;800&display=swap">
<style>
  :root {
    --navy: #0d2f42;
    --accent: #1a8fb8;
    --ink: #4a4f54;
    --mist: #c6e4ee;
    --steel: #c8ced2;
    --paper: #ffffff;
    --edge: #d9dde0;
  }
  * { margin: 0; padding: 0; box-sizing: border-box; }
  html, body {
    width: 1200px; height: 1200px; overflow: hidden;
    background: var(--paper);
    font-family: "Raleway", sans-serif;
  }
  .canvas { position: relative; width: 1200px; height: 1200px; }

  .card {
    position: absolute; left: 280px; width: 624px; height: 347px;
    overflow: hidden;
  }
  .card--front {
    top: 193px; background: var(--navy);
    display: flex; align-items: center; justify-content: center;
  }
  .card--back {
    top: 636px; background: var(--paper);
    border: 1px solid var(--edge);
  }

  .wordmark {
    display: flex; align-items: center; gap: 16px;
    color: var(--paper); font-weight: 700; font-size: 40px;
    letter-spacing: 1px; margin-top: -10px;
  }
  .wordmark__dot {
    width: 18px; height: 18px; border-radius: 50%;
    background: var(--paper);
  }

  .holder { position: absolute; left: 33px; top: 34px; }
  .holder__name {
    color: var(--navy); font-weight: 800; font-size: 31px; line-height: 1;
  }
  .holder__title {
    margin-top: 8px; color: var(--ink); font-weight: 600; font-size: 15.5px;
  }

  .contacts { position: absolute; left: 33px; top: 155px; list-style: none; }
  .contact {
    display: flex; align-items: center; gap: 11px;
    height: 36px; color: var(--ink); font-weight: 500; font-size: 20px;
  }
  .contact svg { width: 21px; height: 21px; flex: none; fill: var(--accent); }

  .tagline {
    position: absolute; left: 33px; top: 282px;
    color: var(--navy); font-weight: 700; font-size: 16px; line-height: 22px;
  }

  .brand-decoration {
    position: absolute; right: 0; bottom: 0; width: 280px; height: 267px;
    background: radial-gradient(circle at 70% 70%, var(--steel) 0%, var(--mist) 55%, rgba(198,228,238,0) 80%);
    opacity: 0.7;
  }
</style>
</head>
<body>
<main class="canvas">
  <section class="card card--front">
    <div class="wordmark">
      <span class="wordmark__dot"></span>
      <span class="wordmark__name">Calmora Advisory Group</span>
    </div>
  </section>

  <section class="card card--back">
    <div class="brand-decoration" role="img" aria-label="Large faint brand symbol decoration"></div>

    <header class="holder">
      <h1 class="holder__name">Dana Weltrup</h1>
      <p class="holder__title">Director General - Aeroespacial y Defensa</p>
    </header>

    <ul class="contacts">
      <li class="contact">
        <svg viewBox="0 0 24 24" aria-hidden="true"><path d="M6.6 10.8a15.1 15.1 0 0 0 6.6 6.6l2.2-2.2c.3-.3.7-.4 1-.2 1.1.4 2.3.6 3.6.6.6 0 1 .4 1 1V20c0 .6-.4 1-1 1A17 17 0 0 1 3 4c0-.6.4-1 1-1h3.5c.6 0 1 .4 1 1 0 1.3.2 2.5.6 3.6.1.3 0 .7-.2 1z"/></svg>
        <span>514-268-3917</span>
      </li>
      <li class="contact">
        <svg viewBox="0 0 24 24" aria-hidden="true"><path d="M2 5h20v14H2z" opacity=".9"/><path d="M2 5l10 8 10-8" fill="none" stroke="#fff" stroke-width="1.8"/></svg>
        <span>dana.weltrup@calmora-example.com</span>
      </li>
      <li class="contact">
        <svg viewBox="0 0 24 24" aria-hidden="true"><circle cx="12" cy="12" r="10"/><path d="M2 12h20M12 2c3 3 3 17 0 20M12 2c-3 3-3 17 0 20M4 7h16M4 17h16" fill="none" stroke="#fff" stroke-width="1.3"/></svg>
        <span>www.calmora-example.com</span>
      </li>
    </ul>

    <p class="tagline">Gestión de propuestas y soporte de captura<br>para compras complejas</p>
  </section>
</main>
</body>
</html>
```